Creative Businesss Card desgin!

Create a business card for our business Gleam window cleaning!
We are open to creative ideas as long as it maintains a professional image.

Target Market(s)

Small Commercial window cleaning clients including car dealerships, strata manager, cafe

Industry/Entity Type

Window Cleaning

Contact Information for Business Card

Daniel Prescott
General Manager
Gleam Window Cleaning

daniel@gleamservices.com.au
pane-care-southbank.com.au
Ph: 1800 GET GLEAM
Mob: 0437 582 061

Colors
fbed22
0392cd

Requirements
Should not have
• Stock window cleaning/ squeegee graphics

```html
<!DOCTYPE html>
<html lang="en">
<head>
<meta charset="utf-8">
<title>Gleam Window Cleaning – Business Cards</title>
<link href="https://fonts.googleapis.com/css2?family=Oswald:wght@300;500&display=swap" rel="stylesheet">
<style>
  :root {
    --backdrop: #323849;
    --brand-yellow: #fbed22;
    --brand-blue: #0392cd;
    --deep-blue: #03628c;
    --navy: #0f5484;
    --navy-dark: #0a4572;
    --ink-blue: #0c4d80;
    --name-blue: #0a86cf;
    --rule-blue: #1a7fcf;
    --paper: #ffffff;
    --ice: #dcefff;
    --shade: #a9abae;
    --gold-light: #f3cf5a;
    --gold-dark: #a86f08;
    --icon-grey: #7f9bb4;
  }
  * { margin: 0; padding: 0; box-sizing: border-box; }
  html, body {
    width: 1200px;
    height: 1130px;
    overflow: hidden;
    background: var(--backdrop);
  }
  .canvas {
    position: relative;
    width: 1200px;
    height: 1130px;
  }
  .card {
    position: absolute;
    left: 209px;
    width: 782px;
    height: 446px;
    overflow: hidden;
    box-shadow: 0 6px 18px rgba(0, 0, 0, 0.45);
  }
  .card--classic { top: 78px; background: var(--paper); }
  .card--gold { top: 606px; background: linear-gradient(90deg, var(--ice) 0%, #e8f4ff 60%, var(--paper) 100%); }
  .card-art {
    position: absolute;
    inset: 0;
    width: 782px;
    height: 446px;
  }
  .brand {
    position: absolute;
    left: 40px;
    top: 22px;
    font-family: "Oswald", sans-serif;
    font-weight: 500;
    color: var(--brand-yellow);
    line-height: 1;
  }
  .brand-name {
    display: block;
    font-size: 54px;
    letter-spacing: 4px;
  }
  .brand-tag {
    display: block;
    font-size: 18px;
    letter-spacing: 1px;
    margin-top: 4px;
  }
  .brand-mark {
    position: absolute;
    left: 244px;
    top: 30px;
    width: 46px;
    height: 46px;
    background: var(--icon-grey);
    border: 2px solid #1d2630;
  }
  .card-info {
    position: absolute;
    top: 24px;
    width: 440px;
    text-align: center;
    font-family: "Oswald", sans-serif;
    font-weight: 300;
    color: var(--ink-blue);
  }
  .card--classic .card-info { left: 351px; }
  .card--gold .card-info { left: 362px; }
  .holder-name {
    font-weight: 500;
    font-size: 49px;
    line-height: 60px;
    color: var(--name-blue);
    letter-spacing: -0.5px;
  }
  .holder-role {
    font-size: 28px;
    line-height: 43px;
    margin-top: 4px;
  }
  .divider {
    width: 340px;
    height: 3px;
    margin: 16px auto 18px;
    background: linear-gradient(90deg, transparent, var(--rule-blue) 12%, var(--rule-blue) 88%, transparent);
  }
  .contact-line {
    font-size: 28px;
    line-height: 50px;
  }
  .phone-line {
    font-size: 28px;
    line-height: 43px;
  }
  .phone-block { margin-top: 12px; }
</style>
</head>
<body>
<div class="canvas">

  <section class="card card--classic">
    <svg class="card-art" viewBox="0 0 782 446" aria-hidden="true">
      <defs>
        <linearGradient id="fold-shade" x1="0" y1="0" x2="1" y2="0">
          <stop offset="0" stop-color="#8e9194"/>
          <stop offset="1" stop-color="#eeeeee"/>
        </linearGradient>
      </defs>
      <polygon points="0,0 367,0 172,242 0,446" fill="var(--brand-blue)"/>
      <polygon points="367,0 399,0 194,245 291,446 268,446 172,242" fill="url(#fold-shade)"/>
      <polygon points="0,446 172,242 268,446" fill="var(--deep-blue)"/>
    </svg>
    <div class="brand">
      <span class="brand-name">GLEAM</span>
      <span class="brand-tag">WINDOW CLEANING</span>
    </div>
    <div class="card-info">
      <h1 class="holder-name">DANIEL PRESCOTT</h1>
      <p class="holder-role">General Manager<br>Gleam Window Cleaning</p>
      <div class="divider"></div>
      <p class="contact-line">daniel@gleamservices.com.au</p>
      <p class="contact-line">pane-care-southbank.com.au</p>
      <div class="phone-block">
        <p class="phone-line">Ph: 1800 GET GLEAM</p>
        <p class="phone-line">Mob: 0437 582 061</p>
      </div>
    </div>
  </section>

  <section class="card card--gold">
    <svg class="card-art" viewBox="0 0 782 446">
      <defs>
        <linearGradient id="gold-band" x1="0" y1="0" x2="1" y2="1">
          <stop offset="0" stop-color="var(--gold-light)"/>
          <stop offset="0.5" stop-color="var(--gold-dark)"/>
          <stop offset="1" stop-color="var(--gold-light)"/>
        </linearGradient>
      </defs>
      <polygon points="0,0 367,0 172,242 0,446" fill="var(--navy)"/>
      <polygon points="0,446 172,242 268,446" fill="var(--navy-dark)"/>
      <polygon role="img" aria-label="Sparkling gold glitter band" points="367,0 399,0 194,245 291,446 268,446 172,242" fill="url(#gold-band)"/>
    </svg>
    <div class="brand">
      <span class="brand-name">GLEAM</span>
      <span class="brand-tag">WINDOW CLEANING</span>
    </div>
    <div class="brand-mark"></div>
    <div class="card-info">
      <h1 class="holder-name">DANIEL PRESCOTT</h1>
      <p class="holder-role">General Manager<br>Gleam Window Cleaning</p>
      <div class="divider"></div>
      <p class="contact-line">daniel@gleamservices.com.au</p>
      <p class="contact-line">pane-care-southbank.com.au</p>
      <div class="phone-block">
        <p class="phone-line">Ph: 1800 GET GLEAM</p>
        <p class="phone-line">Mob: 0437 582 061</p>
      </div>
    </div>
  </section>

</div>
</body>
</html>
```